Velmaran Business Card

Business card for philanthropic organization

Industry/Entity Type

Business

Contact Information for Business Card

Need a very ELEGANT, sober, embossed, formal business card... it should transmit CREDIBILITY. Not looking for a "fun card". would like white, grays or black designs.

Font styles to use
Script

Requirements
Must have
• Embossed look

```html
<!DOCTYPE html>
<html lang="en">
<head>
<meta charset="utf-8">
<title>Velmaran Business Card</title>
<link rel="stylesheet" href="https://fonts.googleapis.com/css2?family=Montserrat:wght@400;600&family=Questrial&display=swap">
<style>
  :root {
    --page-bg: #ecebe8;
    --card-white: #ffffff;
    --silver-light: #f4f4f4;
    --silver-mid: #d2d2d2;
    --silver-dark: #a9a9aa;
    --ink: #4a4a4a;
    --ink-soft: #6d6d6d;
    --accent: #e08a1e;
  }
  html, body {
    margin: 0;
    width: 1200px;
    height: 1000px;
    overflow: hidden;
    background: var(--page-bg);
  }
  .canvas {
    position: relative;
    width: 1200px;
    height: 1000px;
    display: flex;
    flex-direction: column;
    align-items: center;
    justify-content: center;
    gap: 70px;
  }
  .card {
    position: relative;
    width: 560px;
    height: 320px;
    border-radius: 3px;
    overflow: hidden;
    box-shadow: 0 1px 2px rgba(0,0,0,.18), 0 10px 26px rgba(0,0,0,.14);
  }

  /* Front */
  .card-front {
    display: flex;
    background: var(--card-white);
  }
  .front-identity {
    width: 54%;
    padding: 30px 20px 0 30px;
    box-sizing: border-box;
    background: var(--card-white);
  }
  .brand-mark {
    display: flex;
    align-items: center;
    gap: 8px;
    font-family: "Questrial", sans-serif;
    font-size: 15px;
    letter-spacing: .12em;
    color: var(--ink);
    margin-bottom: 22px;
  }
  .brand-dot {
    width: 14px;
    height: 14px;
    border-radius: 50%;
    background: var(--silver-dark);
  }
  .holder-name {
    font-family: "Montserrat", sans-serif;
    font-weight: 600;
    font-size: 22px;
    line-height: 1.1;
    color: var(--accent);
    margin: 0 0 6px;
    white-space: nowrap;
  }
  .holder-role {
    font-family: "Questrial", sans-serif;
    font-size: 17px;
    line-height: 1.2;
    color: var(--ink-soft);
    margin: 0;
  }
  .front-contact {
    flex: 1;
    padding: 30px 24px 0 12px;
    box-sizing: border-box;
    text-align: right;
    background: radial-gradient(ellipse at 38% 62%, var(--silver-light) 0%, var(--silver-mid) 55%, var(--silver-dark) 100%);
    font-family: "Questrial", sans-serif;
    font-size: 13px;
    line-height: 1.6;
    color: var(--ink);
  }
  .front-contact p { margin: 0; white-space: nowrap; }

  /* Back */
  .card-back {
    display: flex;
    flex-direction: column;
    align-items: center;
    justify-content: center;
    gap: 26px;
    background: radial-gradient(ellipse at 55% 40%, #ffffff 0%, var(--silver-mid) 60%, var(--silver-dark) 100%);
  }
  .back-mark {
    font-family: "Questrial", sans-serif;
    font-size: 24px;
    letter-spacing: .2em;
    color: var(--ink);
    display: flex;
    align-items: center;
    gap: 10px;
  }
  .back-mark .brand-dot { width: 18px; height: 18px; }
  .back-email {
    font-family: "Questrial", sans-serif;
    font-size: 11px;
    letter-spacing: .28em;
    text-transform: uppercase;
    color: var(--ink);
  }
</style>
</head>
<body>
<main class="canvas">
  <section class="card card-front" aria-label="Business card front">
    <div class="front-identity">
      <div class="brand-mark"><span class="brand-dot"></span>Velmaran</div>
      <h1 class="holder-name">Teodoro Valdemar</h1>
      <p class="holder-role">Oriel Velmaran</p>
      <p class="holder-role">Potentate 2017</p>
    </div>
    <div class="front-contact">
      <p>0917-04281</p>
      <p>Coral Bay, Republic of Ardena</p>
      <p>+(000)-5550-1234</p>
      <p>teovaldemar@mailbox.example</p>
    </div>
  </section>

  <section class="card card-back" aria-label="Business card back">
    <div class="back-mark"><span class="brand-dot"></span>Velmaran</div>
    <div class="back-email">teovaldemar@mailbox.example</div>
  </section>
</main>
</body>
</html>
```